Business Card Design Project

Business card for new event planning company. I will load in 2 different colors of logs for you to use.

Target Market(s)

meeting planners and business leaders

Industry/Entity Type

Event Planning

Requirements
Must have
• memorable/ creative please - maybe logo on back of the card

Information for business card: (Information may change)

LaVonna Pettibrook
lav@MarigoldOccasionsandGalas.com
www.MarigoldOccasionsandGalas.com
613.275.9042
Nice to have
• Do you think it would be too much to add chirpy, QX, workmesh logo to card to connect?

all are LaVonna Pettibrook

```html
<!DOCTYPE html>
<html lang="en">
<head>
<meta charset="utf-8">
<title>Marigold Occasions and Galas – Business Card</title>
<link rel="stylesheet" href="https://fonts.googleapis.com/css2?family=Open+Sans:wght@400;600&display=swap">
<style>
  :root {
    --card-bg: #ffffff;
    --brand-violet: #7263f5;
    --accent-red: #e8120c;
    --ink: #1c1c1c;
    --on-band: #ffffff;
  }
  html, body {
    margin: 0;
    padding: 0;
    overflow: hidden;
    background: var(--card-bg);
  }
  .card {
    position: relative;
    width: 1200px;
    height: 741px;
    background: var(--card-bg);
    font-family: "Open Sans", sans-serif;
    overflow: hidden;
  }
  .brand-name {
    position: absolute;
    left: 96px;
    top: 128px;
    margin: 0;
    font-size: 62px;
    font-weight: 600;
    line-height: 1.15;
    color: var(--brand-violet);
  }
  .shapes {
    position: absolute;
    inset: 0;
  }
  .identity {
    position: absolute;
    left: 72px;
    top: 512px;
    color: var(--on-band);
  }
  .identity-name {
    font-size: 29px;
    font-weight: 600;
    color: var(--ink);
    margin: 0;
    line-height: 1.2;
  }
  .identity-role {
    font-size: 29px;
    font-weight: 400;
    margin: 12px 0 0;
    line-height: 1.2;
  }
  .contact {
    position: absolute;
    left: 603px;
    top: 478px;
    font-size: 29px;
    line-height: 35px;
    color: var(--ink);
    margin: 0;
    padding: 0;
    list-style: none;
  }
  .contact-label {
    color: var(--accent-red);
  }
</style>
</head>
<body>
  <main class="card">
    <p class="brand-name">Marigold<br>Occasions and Galas</p>

    <svg class="shapes" width="1200" height="741" viewBox="0 0 1200 741" aria-hidden="true">
      <path class="name-band" fill="var(--brand-violet)"
            d="M49 485 H471 L623 641 H79 Q49 641 49 611 Z"/>
      <path class="band-notch" fill="var(--brand-violet)"
            d="M559 485 H585 V508 Z"/>
    </svg>

    <div class="identity">
      <p class="identity-name">LaVonna Pettibrook</p>
      <p class="identity-role">Managing Director</p>
    </div>

    <ul class="contact">
      <li><span class="contact-label">Tel:</span> 613.275.9042</li>
      <li>lav@MarigoldOccasionsandGalas.com</li>
      <li>www.MarigoldOccasionsandGalas.com</li>
    </ul>
  </main>
</body>
</html>
```